Meridale Family Law Firm Website Renovation

We need a website redesign in SquareSpace that is more modern, user friendly, on brand, less cluttered, easier to navigate, conveys clearly what our services are, and has clear, visible calls to action.

We would like to hire and work with the winning designer to complete the remaining pages of the site.

Target Market(s)

Couples looking for divorce representation or mediation who have a conscious, progressive mindset. They are self-aware and personal development plays an important role in their lives. They want an amicable interaction and aspire to have a healthy relationship after divorce.

Age range: 30-60
Income 100K+ household

Industry/Entity Type

Family Law

Font styles to use
Sans Serif

Colors
85acd3
33a6d7
50c0af
a0cd3a

Requirements
Must have
• Please see attached doc for full creative brief details.

"Changing the way people divorce" on top of site.
Images that show happy clients and that represent males and females. Diversity inclusion is also be important.
We are looking for warm, welcoming design and imagery.
Should not have
• Not heavily attorney focused.
Please see attached brief for full description.

```html
<!DOCTYPE html>
<html lang="en">
<head>
<meta charset="utf-8">
<title>Meridale Family Law &amp; Mediation</title>
<link href="https://fonts.googleapis.com/css2?family=Montserrat:wght@300;400;500;600&display=swap" rel="stylesheet">
<style>
:root{
  --blue:#3a8ee6;
  --green:#5cc561;
  --orange:#ec6f2d;
  --ink:#333a42;
  --muted:#6b7078;
  --footer:#272a31;
  --white:#ffffff;
}
*{box-sizing:border-box;margin:0;padding:0}
html,body{width:1200px;height:4693px;overflow:hidden}
body{font-family:'Montserrat',sans-serif;color:var(--ink);background:var(--white);position:relative}
.abs{position:absolute}
section{position:absolute;left:0;width:1200px;overflow:hidden}
.btn{position:absolute;display:flex;align-items:center;justify-content:center;color:#fff;font-size:10.5px;font-weight:600;letter-spacing:.3px;text-transform:uppercase}
.btn-blue{background:var(--blue)}
.btn-orange{background:var(--orange)}
.btn-green{background:var(--green)}
.rule{position:absolute;height:3px;width:44px}
h2{font-weight:300;font-size:25px;line-height:1.25;color:var(--ink)}
p.body{font-size:11.5px;line-height:1.75;color:var(--muted)}

/* header + hero */
.hero{top:0;height:665px;background:linear-gradient(180deg,#d6e6f5 0%,#e8f1f9 60%,#f4f8fb 100%)}
.hero-photo{left:440px;top:0;width:760px;height:665px;background:
  linear-gradient(90deg,rgba(232,241,249,1) 0%,rgba(232,241,249,0) 14%),
  linear-gradient(165deg,#cfe1f1 0%,#c9dbea 22%,#d8b39b 40%,#b7856b 58%,#8c6654 72%,#c6d3df 88%,#e3ecf4 100%)}
.nav{top:53px;font-size:11px;color:var(--ink);display:flex;gap:26px}
.brand{left:500px;top:18px;width:200px;text-align:center}
.brand-mark{width:60px;height:60px;border-radius:50%;background:#2e8c5e;margin:0 auto 10px}
.brand-name{font-size:13px;font-weight:500;letter-spacing:2.5px;color:var(--ink);line-height:1.4}
.brand-sub{font-size:8px;letter-spacing:2px;color:var(--muted)}
.hero h1{left:233px;top:238px;font-weight:300;font-size:45px;line-height:1.06;color:var(--ink)}
.hero .note{left:235px;top:356px;font-size:10.5px;font-style:italic;color:var(--muted)}
.hero .phone{left:235px;top:374px;width:187px;height:43px;font-size:18px;font-weight:500;text-transform:none;letter-spacing:0}

/* intro */
.intro{top:665px;height:551px}
.collage{position:absolute}

/* services */
.services{top:1216px;height:561px;background:#2c3036}
.card{position:absolute;top:95px;width:353px;height:372px;background:#fff;text-align:center}
.card h3{margin-top:55px;font-weight:300;font-size:23px;color:var(--ink)}
.card .rule{left:155px;top:98px}
.card p{position:absolute;left:35px;right:35px;top:122px;font-size:10.5px;line-height:1.8;color:var(--muted)}
.card .btn{left:100px;top:279px;width:156px;height:37px}

/* questions */
.questions{top:1777px;height:346px;background:linear-gradient(180deg,#eef1f5,#e3e8ee 50%,#f2f4f7)}
.center{position:absolute;left:0;width:1200px;text-align:center}

/* video band */
.video-band{top:2123px;height:439px;background:var(--green)}
.video{position:absolute;border:6px solid #fff;box-shadow:0 4px 14px rgba(0,0,0,.18)}
.play{position:absolute;left:50%;top:50%;width:38px;height:38px;margin:-19px 0 0 -19px}

/* mediation */
.mediation{top:2562px;height:525px;background:#fff}

/* harm */
.harm{top:3087px;height:482px;background:#fff}

/* testimonials */
.testimonials{top:3569px;height:384px;background:#f4f5f7}
.quote-card{left:588px;top:128px;width:377px;height:160px;background:#fff;box-shadow:0 3px 14px rgba(0,0,0,.08)}

/* awards */
.awards{top:3953px;height:308px;background:#2f7dd4}
.badge{position:absolute;top:95px;width:131px;height:131px;background:#fff;display:flex;align-items:center;justify-content:center}

/* footer */
.footer{top:4261px;height:432px;background:var(--footer);color:#c4c7cd}
.footer h4{font-size:11.5px;font-weight:500;color:#e7e9ec}
.footer .col-rule{position:absolute;height:2px;width:40px;background:var(--blue)}
.footer .links{font-size:10px;line-height:25px;color:#a8acb3}
.social{position:absolute;width:32px;height:32px;background:#3a3e46}
</style>
</head>
<body>

<section class="hero">
  <div class="abs hero-photo" role="img" aria-label="Smiling father carrying his young son on his shoulders against a bright sky"></div>
  <nav class="abs nav" style="left:268px"><span>Home</span><span>About</span><span>Services</span><span>Resources</span></nav>
  <nav class="abs nav" style="left:701px;top:51px"><span>Testimonials</span><span>FAQ</span><span>Schedule</span><span>Contact</span></nav>
  <div class="abs brand">
    <div class="brand-mark"></div>
    <div class="brand-name">MERIDALE<br>FAMILY</div>
    <div class="brand-sub">LAW &amp; MEDIATION</div>
  </div>
  <h1 class="abs">Changing the Way<br>People Divorce.</h1>
  <div class="abs note">Schedule a free information call</div>
  <div class="btn btn-blue phone">(303) 555-0187</div>
</section>

<section class="intro">
  <div class="collage" style="left:182px;top:92px;width:174px;height:172px;background:linear-gradient(150deg,#5b4a42 0%,#9c7864 45%,#d8c1ae 100%)" role="img" aria-label="Family reviewing papers together at a table"></div>
  <div class="collage" style="left:312px;top:176px;width:174px;height:172px;border:4px solid #fff;background:linear-gradient(150deg,#e6d8cc 0%,#b99780 50%,#7d6456 100%)" role="img" aria-label="Parents talking with their child on a sofa"></div>
  <div class="collage" style="left:233px;top:286px;width:174px;height:172px;border:4px solid #fff;border-top:0;background:linear-gradient(150deg,#3f4a52 0%,#8e7466 50%,#d1b59f 100%)" role="img" aria-label="Young girl hugging a teddy bear"></div>
  <h2 class="abs" style="left:528px;top:125px">Efficient and positive family legal<br>transitions without costly,<br>painful legal battles.</h2>
  <div class="rule" style="left:530px;top:234px;background:var(--orange)"></div>
  <p class="abs body" style="left:530px;top:252px;width:430px">Traditionally, divorcing couples had two options: hire lawyers and go to battle, or avoid divorce professionals.</p>
  <p class="abs body" style="left:530px;top:306px;width:430px">Many people don't want to add unnecessary financial and emotional costs to their divorce, but they need professional help to ensure they come away confident, and highly effective advice with a good parenting plan and fair financial outcomes.</p>
  <div class="btn btn-orange" style="left:530px;top:395px;width:251px;height:42px">Schedule a free information call</div>
</section>

<section class="services">
  <div class="abs" style="left:0;top:0;width:1200px;height:561px;background:linear-gradient(90deg,#4a423f 0%,#33373d 30%,#2a2e34 55%,#4b4442 80%,#3a3638 100%)" role="img" aria-label="Dim photo of a couple meeting with a mediator"></div>
  <div class="abs" style="left:0;top:400px;width:1200px;height:161px;background:linear-gradient(180deg,rgba(0,0,0,0),rgba(20,22,26,.45))"></div>
  <div class="card" style="left:233px">
    <svg class="abs" style="right:0;top:0" width="26" height="26"><polygon points="0,0 26,0 26,26" fill="#3a8ee6"/></svg>
    <svg class="abs" style="left:0;bottom:0" width="26" height="26"><polygon points="0,0 26,26 0,26" fill="#3a8ee6"/></svg>
    <h3>Work Together</h3>
    <div class="rule" style="background:var(--blue)"></div>
    <p>Mediation is possible when both spouses are willing to negotiate their divorce agreements in good faith, with the help of a neutral mediator. Meridale Family&trade; attorney-mediators are experienced family lawyers and are skilled at helping clients reach fair, workable agreements, without the cost and damage of the conventional divorce process.</p>
    <div class="btn btn-blue">Learn more</div>
  </div>
  <div class="card" style="left:610px">
    <svg class="abs" style="right:0;top:0" width="26" height="26"><polygon points="0,0 26,0 26,26" fill="#5cc561"/></svg>
    <svg class="abs" style="left:0;bottom:0" width="26" height="26"><polygon points="0,0 26,26 0,26" fill="#5cc561"/></svg>
    <h3>Help Just For You</h3>
    <div class="rule" style="background:var(--green)"></div>
    <p>If mediation is not possible, you need a lawyer to advise, negotiate, and possibly advocate for you. Our experienced Meridale Family&trade; lawyers offer clear, confident, and highly effective advice and representation while attempting to minimize financial and emotional costs to you and your family.</p>
    <div class="btn btn-green">Learn more</div>
  </div>
</section>

<section class="questions">
  <div class="abs" style="left:0;top:0;width:1200px;height:346px;background:linear-gradient(90deg,rgba(255,255,255,.6) 0%,rgba(214,221,230,.5) 35%,rgba(205,213,223,.55) 55%,rgba(255,255,255,.6) 100%)" role="img" aria-label="Faded city skyline in soft fog"></div>
  <h2 class="center" style="top:94px">Get your questions answered</h2>
  <div class="rule" style="left:578px;top:134px;background:var(--blue)"></div>
  <p class="center body" style="top:145px">Lorem Ipsum is simply dummy text of the printing and typesetting industry.<br>lorem ipsum has been the industry's standard.</p>
  <div class="btn btn-blue" style="left:475px;top:210px;width:252px;height:42px">Schedule a free information call</div>
</section>

<section class="video-band">
  <h2 class="abs" style="left:157px;top:110px;color:#fff">Divorce doesn't have<br>to be traumatic.</h2>
  <div class="rule" style="left:157px;top:190px;background:var(--orange)"></div>
  <p class="abs body" style="left:157px;top:202px;width:390px;color:#eaf7ea">Lorem Ipsum is simply dummy text of the printing and typesetting industry. lorem ipsum has been.</p>
  <div class="btn btn-orange" style="left:157px;top:255px;width:251px;height:42px">Schedule a free information call</div>
  <div class="video" style="left:605px;top:73px;width:438px;height:293px;background:linear-gradient(180deg,#9a9c9f 0%,#7c7e81 45%,#4a4c4f 70%,#2f3133 100%)" role="img" aria-label="Black and white video still of a mother walking with two children on a beach">
    <svg class="play" viewBox="0 0 38 38"><circle cx="19" cy="19" r="19" fill="#fff"/><polygon points="15,12 27,19 15,26" fill="#e8592b"/></svg>
  </div>
</section>

<section class="mediation">
  <div class="abs" style="left:0;top:150px;width:1200px;height:375px;background:linear-gradient(180deg,rgba(255,255,255,1) 0%,rgba(255,255,255,0) 35%),linear-gradient(90deg,#8a7467 0%,#c9b8aa 14%,#6d7683 28%,#d6c4b6 42%,#b59885 56%,#e3d2c5 70%,#7a6f6c 86%,#c8b9ad 100%)" role="img" aria-label="Group of diverse adults sitting in a circle during a mediation session"></div>
  <h2 class="center" style="top:93px">Mediation or Lawyer?</h2>
  <div class="rule" style="left:578px;top:133px;background:var(--blue)"></div>
  <p class="center body" style="top:145px">Our simple, free questionnaire can help you determine if you and your spouse are<br>suited for mediation, or if you may want legal representation for yourself.</p>
  <div class="btn btn-blue" style="left:475px;top:208px;width:250px;height:42px">Take our free questionnaire</div>
</section>

<section class="harm">
  <div class="abs" style="left:0;top:0;width:379px;height:482px;background:var(--orange)"></div>
  <div class="video" style="left:158px;top:96px;width:434px;height:291px;background:linear-gradient(90deg,#2e3033 0%,#55575a 40%,#6a6c6f 60%,#3a3c3f 100%)" role="img" aria-label="Black and white video still of a man speaking in his office">
    <svg class="play" viewBox="0 0 38 38"><circle cx="19" cy="19" r="19" fill="#fff"/><polygon points="15,12 27,19 15,26" fill="#e8592b"/></svg>
  </div>
  <h2 class="abs" style="left:659px;top:130px">Avoiding harm to<br>children in divorce</h2>
  <div class="rule" style="left:661px;top:201px;background:var(--orange)"></div>
  <p class="abs body" style="left:661px;top:218px;width:390px">There are many variations of passages of Lorem Ipsum available, but the majority have suffered alteration in some form, by injected humour, or randomised words which don't look even slightly believable.</p>
  <div class="btn btn-orange" style="left:661px;top:313px;width:250px;height:42px">Take our free questionnaire</div>
</section>

<section class="testimonials">
  <h2 class="abs" style="left:233px;top:147px">What people say<br>about us</h2>
  <div class="rule" style="left:235px;top:219px;background:var(--orange)"></div>
  <p class="abs body" style="left:235px;top:237px;width:250px">Learn how our unique mediation process has helped others.</p>
  <div class="abs quote-card">
    <div class="abs" style="left:20px;top:18px;width:40px;height:40px;border-radius:50%;background:linear-gradient(135deg,#b89a86,#e9ddd4)" role="img" aria-label="Client portrait"></div>
    <div class="abs" style="left:70px;top:24px;font-size:12px;color:var(--green)">Divorce Mediation Client</div>
    <svg class="abs" style="left:70px;top:42px" width="62" height="10" viewBox="0 0 62 10"><g fill="#f2b705"><polygon points="5,0 6.2,3.6 10,3.6 7,5.8 8.1,9.5 5,7.2 1.9,9.5 3,5.8 0,3.6 3.8,3.6"/><polygon transform="translate(13 0)" points="5,0 6.2,3.6 10,3.6 7,5.8 8.1,9.5 5,7.2 1.9,9.5 3,5.8 0,3.6 3.8,3.6"/><polygon transform="translate(26 0)" points="5,0 6.2,3.6 10,3.6 7,5.8 8.1,9.5 5,7.2 1.9,9.5 3,5.8 0,3.6 3.8,3.6"/><polygon transform="translate(39 0)" points="5,0 6.2,3.6 10,3.6 7,5.8 8.1,9.5 5,7.2 1.9,9.5 3,5.8 0,3.6 3.8,3.6"/><polygon transform="translate(52 0)" points="5,0 6.2,3.6 10,3.6 7,5.8 8.1,9.5 5,7.2 1.9,9.5 3,5.8 0,3.6 3.8,3.6"/></g></svg>
    <p class="abs" style="left:20px;top:80px;width:340px;font-size:11px;line-height:1.7;color:var(--ink)">"I am so grateful for my experience with Meridale Family Law &amp; Mediation. I learned so much about myself and my capacity to love, grieve, and heal. You were so great at</p>
  </div>
  <svg class="abs" style="left:753px;top:312px" width="50" height="14" viewBox="0 0 50 14"><g fill="none" stroke-width="1.6" stroke-linecap="round"><path d="M2 7h16M7 2L2 7l5 5" stroke="#3a8ee6"/><path d="M32 7h16M43 2l5 5-5 5" stroke="#333a42"/></g></svg>
</section>

<section class="awards">
  <div class="abs" style="left:0;top:0;width:1200px;height:308px;background:linear-gradient(90deg,#2a6fbd 0%,#3584d9 30%,#2c78c9 60%,#2669b5 100%)" role="img" aria-label="Blue-tinted photo of a busy office"></div>
  <div class="badge" style="left:246px"><div style="width:90px;height:60px;background:#1f4f8f;border-radius:4px"></div></div>
  <div class="badge" style="left:390px"><div style="width:70px;height:70px;background:#f08a24;border-radius:50%"></div></div>
  <div class="badge" style="left:534px"><div style="width:74px;height:74px;background:#5a3a8c;border-radius:50%"></div></div>
  <div class="badge" style="left:679px"><div style="width:62px;height:62px;background:#d8a42a;border-radius:50%"></div></div>
  <div class="badge" style="left:823px"><div style="width:84px;height:44px;background:#2b6fc0;border-radius:4px"></div></div>
</section>

<section class="footer">
  <div class="center" style="top:93px;font-size:17px;font-weight:300;color:#fff">We are proud to serve your family</div>
  <div class="abs" style="left:578px;top:123px;height:2px;width:44px;background:var(--blue)"></div>
  <p class="center" style="top:141px;font-size:10px;line-height:1.75;color:#8f949c">Meridale Family Law &amp; Mediation LLC currently serves the legal needs of Colorado residents (including same-sex and other alternative<br>families) in Boulder County, Denver County, Broomfield County, Larimer County, Adams County, Weld County, and Jefferson County.</p>

  <h4 class="abs" style="left:233px;top:216px">Quick Links</h4>
  <div class="col-rule" style="left:233px;top:236px"></div>
  <div class="abs links" style="left:233px;top:248px">Home<br>About<br>Services<br>Resources</div>
  <div class="abs links" style="left:332px;top:248px">Testimonials<br>FAQ<br>Schedule<br>Contact</div>

  <h4 class="abs" style="left:484px;top:216px">Contact Information</h4>
  <div class="col-rule" style="left:484px;top:236px"></div>
  <div class="abs links" style="left:484px;top:252px;line-height:33px">
    <div style="display:flex;align-items:center;gap:10px"><svg width="16" height="16" viewBox="0 0 16 16"><rect width="16" height="16" fill="#3a8ee6"/><path d="M5 4l2 2-1 1.5c.6 1.2 1.3 1.9 2.5 2.5L10 9l2 2-1.2 1.2C7.5 12 4 8.5 3.8 5.2z" fill="#fff"/></svg>1+ (303) 555-0187</div>
    <div style="display:flex;align-items:center;gap:10px"><svg width="16" height="16" viewBox="0 0 16 16"><rect width="16" height="16" fill="#3a8ee6"/><rect x="3.5" y="5" width="9" height="6" fill="none" stroke="#fff"/><path d="M3.5 5l4.5 3.5L12.5 5" fill="none" stroke="#fff"/></svg>hello@meridalefamilylaw.com</div>
    <div style="display:flex;align-items:center;gap:10px"><svg width="16" height="16" viewBox="0 0 16 16"><rect width="16" height="16" fill="#3a8ee6"/><path d="M8 3a3 3 0 0 1 3 3c0 2.2-3 6-3 6S5 8.2 5 6a3 3 0 0 1 3-3z" fill="#fff"/><circle cx="8" cy="6" r="1" fill="#3a8ee6"/></svg>LLC 1420 Aspen Ridge Road, Suite 2 Boulder, Colorado 80302</div>
  </div>

  <h4 class="abs" style="left:883px;top:216px">Social Media</h4>
  <div class="col-rule" style="left:883px;top:236px"></div>
  <div class="social" style="left:883px;top:258px"></div>
  <div class="social" style="left:927px;top:258px;background:var(--blue)"></div>
  <div class="social" style="left:883px;top:298px"></div>
  <div class="social" style="left:927px;top:298px"></div>

  <div class="abs" style="left:233px;top:399px;font-size:9.5px;color:#8f949c">Website content copyright 2014-2020 Meridale Family Law &amp; Mediation LLC</div>
  <svg class="abs" style="left:938px;top:398px" width="27" height="18" viewBox="0 0 27 18"><rect y="0" width="27" height="3" fill="#e40303"/><rect y="3" width="27" height="3" fill="#ff8c00"/><rect y="6" width="27" height="3" fill="#ffed00"/><rect y="9" width="27" height="3" fill="#008026"/><rect y="12" width="27" height="3" fill="#004dff"/><rect y="15" width="27" height="3" fill="#750787"/></svg>
</section>

</body>
</html>
```